KTLwave Power Point Template for Presentations

KTLwave, a leading provider of data to the sports industry is in need of a new look for our Power Point presentations. I added the one we have been using. I want a better cover slide and then a variety of slides that can be used to accommodate bullet points, graphs and charts. I want to stick with our basic color palette of orange and blue as that is the colors we use. I caution you that I don't want to see people playing sports. Our data is used for marketing-oriented analysis and I want that message to come across in a modern and almost fun way. I have attached a report that we did last year. That is what I want to get away from.

```html
<!DOCTYPE html>
<html lang="en">
<head>
<meta charset="utf-8">
<title>KTLwave Presentation Template</title>
<link href="https://fonts.googleapis.com/css2?family=Poppins:wght@400;500;600&family=Roboto:wght@500;700&display=swap" rel="stylesheet">
<style>
:root{
  --stage:#9b9b9b;
  --blue:#2f44b0;
  --violet:#4a2595;
  --navy:#2c2a8c;
  --orange:#f07f1a;
  --orange-dark:#d86c0c;
  --paper:#f7f7fb;
  --white:#ffffff;
  --ink:#222233;
  --grid:#e4e4ee;
  --bar-a:#3b2597;
  --bar-b:#1a86d0;
}
*{box-sizing:border-box;margin:0;padding:0}
html,body{width:1026px;height:1200px;overflow:hidden;background:var(--stage)}
body{position:relative;font-family:"Poppins",sans-serif;color:var(--ink)}
.slide{position:absolute;width:443px;height:249px;overflow:hidden;background:var(--paper);box-shadow:0 6px 14px rgba(0,0,0,.25)}
.slide--dark{background:linear-gradient(120deg,var(--blue) 0%,#3a36a8 50%,var(--violet) 100%);color:var(--white)}
.col-l{left:51px}.col-r{left:531px}
.row-1{top:54px}.row-2{top:335px}.row-3{top:616px}.row-4{top:897px}

/* brand */
.brand{position:absolute;display:flex;align-items:center;gap:4px;font-family:"Poppins",sans-serif;font-weight:600;font-size:15px;letter-spacing:-.3px;color:var(--navy)}
.brand__dot{width:20px;height:20px;border-radius:50%;border:2.5px solid var(--orange)}
.slide--dark .brand{color:var(--white)}
.slide--dark .brand__dot{border-color:var(--white)}
.brand--tr{top:13px;right:26px}

/* header band */
.band{position:absolute;left:0;top:11px;width:302px;height:25px;background:linear-gradient(90deg,var(--blue),var(--violet));border-radius:0 13px 13px 0;color:var(--white);font-family:"Roboto",sans-serif;font-weight:700;font-size:11.5px;line-height:25px;padding-left:26px}

/* footer */
.foot{position:absolute;left:25px;top:228px;width:393px;height:17px;border-radius:9px;background:var(--orange);color:var(--white);font-size:5.2px;display:flex;align-items:center;padding-left:8px;gap:6px}
.foot__sep{opacity:.8}
.foot__num{position:absolute;right:3px;top:2.5px;width:12px;height:12px;border-radius:50%;background:var(--white);color:var(--navy);font-weight:600;font-size:5px;display:flex;align-items:center;justify-content:center}
.slide--dark .foot{background:var(--white);color:var(--navy)}
.slide--dark .foot__num{background:var(--orange);color:var(--white)}
.foot__ico{color:var(--orange);margin-right:2px}
.slide--dark .foot__ico{color:var(--orange)}

/* cover */
.cover__photo{position:absolute;left:39px;top:47px;width:155px;height:155px;border-radius:50%;background:radial-gradient(circle at 40% 40%,#9aa8d8,#3c45a6 70%);border:3px solid rgba(255,255,255,.55)}
.cover__title{position:absolute;left:227px;top:76px;font-family:"Roboto",sans-serif;font-weight:700;font-size:17.5px;line-height:20px}
.cover__rule{position:absolute;left:227px;top:137px;width:28px;height:2px;background:var(--orange)}
.cover__sub{position:absolute;left:227px;top:148px;font-size:9.5px;line-height:12.5px}

/* agenda */
.agenda__brand{top:21px;left:25px}
.agenda__title{position:absolute;left:31px;top:62px;font-family:"Roboto",sans-serif;font-weight:700;font-size:16px;color:var(--navy)}
.pill{position:absolute;left:25px;height:22px;border-radius:11px;background:var(--white);box-shadow:0 2px 5px rgba(40,40,90,.15);font-size:6.4px;font-weight:600;display:flex;align-items:center;padding-left:10px}
.pill__go{position:absolute;right:9px;top:6.5px;width:9px;height:9px;border-radius:50%;background:var(--orange);color:var(--white);font-size:5px;display:flex;align-items:center;justify-content:center}
.agenda__frame{position:absolute;left:246px;top:21px}
.agenda__photo{position:absolute;left:264px;top:34px;width:141px;height:170px;background:linear-gradient(150deg,#f4b067,#d9691d 45%,#6a4b55)}

/* about */
.about__lead{position:absolute;left:40px;width:363px;top:48px;text-align:center;color:var(--navy);font-weight:600;font-size:8.2px;line-height:11px}
.about__copy{position:absolute;left:55px;width:333px;text-align:center;font-size:5.8px;line-height:8.8px}
.bio{position:absolute;top:137px;width:189px;height:77px;border-radius:18px;background:var(--white);box-shadow:0 2px 6px rgba(40,40,90,.15)}
.bio__photo{position:absolute;top:152px;width:50px;height:50px;border-radius:50%;border:2px solid var(--orange);background:linear-gradient(160deg,#d8d3cc,#7f8a9a)}
.bio__text{position:absolute;font-size:4.3px;line-height:6.6px}
.bio__text b{color:var(--navy)}

/* what we do */
.hub__label{position:absolute;font-size:6.4px;font-weight:600;line-height:9px}
.hub__icon{position:absolute;width:22px;height:22px;border-radius:50%;background:var(--white);box-shadow:0 1px 5px rgba(40,40,90,.2);display:flex;align-items:center;justify-content:center}
.hub__core{position:absolute;left:166px;top:82px;width:110px;height:110px;border-radius:50%;border:9px solid var(--navy);background:var(--white);text-align:center;padding-top:48px;color:var(--blue);font-size:5.4px;font-weight:600;line-height:8.6px}
.hub__core-dot{position:absolute;left:36px;top:7px;width:20px;height:20px;border-radius:50%;border:2.5px solid var(--orange)}

/* divider */
.divider__title{position:absolute;left:0;width:443px;top:104px;text-align:center;font-family:"Roboto",sans-serif;font-weight:700;font-size:28px;letter-spacing:.3px}

/* chart */
.chart__cap{position:absolute;left:0;width:443px;top:48px;text-align:center;color:var(--navy);font-weight:500;font-size:8.2px}
.chart{position:absolute;left:66px;top:68px}

/* exec summary */
.card{position:absolute;top:76px;width:170px;height:130px;border-radius:5px;background:var(--white);box-shadow:0 2px 6px rgba(40,40,90,.15)}
.card--blue{left:44px;border:1px solid var(--bar-b)}
.card--orange{left:229px;border:1px solid var(--orange)}
.card__badge{position:absolute;top:-17px;left:12px;width:34px;height:34px;border-radius:50%;border:2px solid var(--white);display:flex;align-items:center;justify-content:center}
.card--blue .card__badge{background:var(--bar-b)}
.card--orange .card__badge{background:var(--orange)}
.card__head{position:absolute;left:12px;top:26px;font-size:6.6px;font-weight:600;color:var(--navy)}
.card__body{position:absolute;left:12px;top:38px;width:146px;font-size:5px;line-height:8.2px}

/* contact */
.info__title{position:absolute;left:25px;top:51px;font-family:"Roboto",sans-serif;font-weight:700;font-size:17.5px;line-height:20px}
.info__rule{position:absolute;left:25px;top:95px;width:28px;height:2px;background:var(--orange)}
.info__copy{position:absolute;left:25px;top:104px;width:180px;font-size:5.7px;line-height:9.2px;text-align:justify}
.info__price{position:absolute;left:25px;top:189px;font-size:9.6px}
.info__price b{color:var(--orange);font-weight:600}
.info__split{position:absolute;left:232px;top:50px;width:1px;height:144px;background:rgba(255,255,255,.8)}
.info__row{position:absolute;left:255px;display:flex;align-items:center;gap:9px;font-size:7.8px;line-height:11px}
.info__ico{flex:none;width:22px;height:22px;border-radius:50%;background:var(--white);display:flex;align-items:center;justify-content:center}
</style>
</head>
<body>

<!-- 01 cover -->
<section class="slide slide--dark col-l row-1">
  <div class="brand brand--tr"><span class="brand__dot"></span>KTLwave</div>
  <div class="cover__photo" role="img" aria-label="Analyst reviewing a sports data dashboard on a laptop"></div>
  <h1 class="cover__title">SPORTS FANDOM<br>IN A POST-PANDEMIC<br>WORLD</h1>
  <div class="cover__rule"></div>
  <p class="cover__sub">2021 Annual Study of Sports Fan Habits<br>and Behaviors</p>
  <div class="foot"><span><span class="foot__ico">&#9742;</span>555-010-4821</span><span class="foot__sep">|</span><span><span class="foot__ico">&#9993;</span>info@ktlwave.com</span><span class="foot__sep">|</span><span><span class="foot__ico">&#9679;</span>https://fanmetricsdata.com</span><span class="foot__num">01</span></div>
</section>

<!-- 02 agenda -->
<section class="slide col-r row-1">
  <div class="brand agenda__brand"><span class="brand__dot"></span>KTLwave</div>
  <h2 class="agenda__title">AGENDA</h2>
  <div class="pill" style="top:93px;width:132px">ABOUT US<span class="pill__go">&rsaquo;</span></div>
  <div class="pill" style="top:123px;width:148px">FANTASY SPORTS ENGAGEMENT<span class="pill__go">&rsaquo;</span></div>
  <div class="pill" style="top:155px;width:181px">SPORTS FAN SOCIAL MEDIA ENGAGEMENT<span class="pill__go">&rsaquo;</span></div>
  <div class="pill" style="top:185px;width:148px">SURVEY METHODOLOGY<span class="pill__go">&rsaquo;</span></div>
  <svg class="agenda__frame" width="174" height="146" viewBox="0 0 174 146"><polygon points="0,0 174,0 174,146 166,139 166,8 10,8" fill="var(--navy)"/></svg>
  <div class="agenda__photo" role="img" aria-label="Hands using a laptop showing orange analytics charts"></div>
  <div class="foot"><span><span class="foot__ico" style="color:#fff">&#9742;</span>555-010-4821</span><span class="foot__sep">|</span><span>&#9993; info@ktlwave.com</span><span class="foot__sep">|</span><span>&#9679; https://fanmetricsdata.com</span><span class="foot__num">02</span></div>
</section>

<!-- 03 about -->
<section class="slide col-l row-2">
  <div class="band">ABOUT US</div>
  <div class="brand brand--tr"><span class="brand__dot"></span>KTLwave</div>
  <p class="about__lead">Leading provider of sports market analytics and sports<br>marketing research in the US</p>
  <p class="about__copy" style="top:76px">Comprehensive online platform of nationwide sports marketing analytics, using syndicated and custom proprietary research for the professional and college sports, consumer research, industry reports, and licensed industry articles.</p>
  <p class="about__copy" style="top:107px">Extensive research and custom reports covering sports participation, the fan market and behaviors, venues, sponsorships, and expenditure on sporting goods, brand preference and more.</p>
  <div class="bio" style="left:75px;width:150px"></div>
  <div class="bio__photo" role="img" aria-label="Portrait of Dale Hartman" style="left:26px"></div>
  <p class="bio__text" style="left:83px;top:145px;width:120px"><b>Dale Hartman</b> has over twenty years of marketing and consumer research experience across sports, fitness and active lifestyle categories. He has led research teams at several industry groups, speaks at conferences and events, and is respected by financial and investment firms and leading brands in sports footwear and apparel.</p>
  <div class="bio" style="left:278px;width:140px"></div>
  <div class="bio__photo" role="img" aria-label="Portrait of Glen Porter" style="left:229px"></div>
  <p class="bio__text" style="left:286px;top:155px;width:122px"><b>Glen Porter</b> is a former editor and publisher in sports business and a founder of a large B2B conference and trade show. He sold the event in 2018 and now runs a consulting business whose clients include global companies in the active lifestyle business.</p>
  <div class="foot"><span>&#9742; 555-010-4821</span><span class="foot__sep">|</span><span>&#9993; info@ktlwave.com</span><span class="foot__sep">|</span><span>&#9679; https://fanmetricsdata.com</span><span class="foot__num">03</span></div>
</section>

<!-- 04 what we do -->
<section class="slide col-r row-2">
  <div class="band">WHAT WE DO</div>
  <div class="brand brand--tr"><span class="brand__dot"></span>KTLwave</div>
  <svg style="position:absolute;left:0;top:0" width="443" height="249" viewBox="0 0 443 249">
    <g fill="none" stroke="#9a9ab0" stroke-width=".6">
      <polyline points="135,74 166,74 186,94"/>
      <polyline points="135,137 166,137"/>
      <polyline points="135,200 166,200 186,180"/>
      <polyline points="307,74 276,74 256,94"/>
      <polyline points="307,137 276,137"/>
      <polyline points="307,200 276,200 256,180"/>
    </g>
    <g fill="#fff" stroke="#9a9ab0" stroke-width=".6">
      <circle cx="186" cy="94" r="2"/><circle cx="166" cy="137" r="2"/><circle cx="186" cy="180" r="2"/>
      <circle cx="256" cy="94" r="2"/><circle cx="276" cy="137" r="2"/><circle cx="256" cy="180" r="2"/>
    </g>
  </svg>
  <div class="hub__core"><span class="hub__core-dot"></span>THE SIX ELEMENTS<br>FOR SPORTS FANDOM<br>IN A POST PANDEMIC<br>WORLD</div>
  <div class="hub__icon" style="left:113px;top:63px"><svg width="12" height="12"><circle cx="6" cy="6" r="4.5" fill="none" stroke="var(--orange)"/></svg></div>
  <div class="hub__icon" style="left:113px;top:126px"><svg width="12" height="12"><rect x="2" y="2" width="8" height="8" fill="none" stroke="var(--orange)"/></svg></div>
  <div class="hub__icon" style="left:113px;top:189px"><svg width="12" height="12"><path d="M2 10V5M6 10V2M10 10V6" stroke="var(--orange)" stroke-width="1.5"/></svg></div>
  <div class="hub__icon" style="left:296px;top:63px"><svg width="12" height="12"><rect x="1.5" y="2.5" width="9" height="6" fill="none" stroke="var(--orange)"/><path d="M5 5l2 1-2 1z" fill="var(--orange)"/></svg></div>
  <div class="hub__icon" style="left:296px;top:126px"><svg width="12" height="12"><path d="M6 1.5l4 2v3c0 2-2 3.5-4 4-2-.5-4-2-4-4v-3z" fill="none" stroke="var(--orange)"/></svg></div>
  <div class="hub__icon" style="left:296px;top:189px"><svg width="12" height="12"><circle cx="6" cy="6" r="4.5" fill="none" stroke="var(--orange)"/><circle cx="6" cy="6" r="1.8" fill="var(--orange)"/></svg></div>
  <span class="hub__label" style="left:69px;top:70px">FANDOM</span>
  <span class="hub__label" style="left:66px;top:133px">E-SPORTS</span>
  <span class="hub__label" style="left:30px;top:190px;text-align:right;width:72px">SOCIAL<br>MEDIA ENGAGEMENT</span>
  <span class="hub__label" style="left:331px;top:70px">STREAMING MEDIA</span>
  <span class="hub__label" style="left:331px;top:133px">FANTASY SPORTS</span>
  <span class="hub__label" style="left:331px;top:196px">GAMBLING ON SPORTS</span>
  <div class="foot"><span>&#9742; 555-010-4821</span><span class="foot__sep">|</span><span>&#9993; info@ktlwave.com</span><span class="foot__sep">|</span><span>&#9679; https://fanmetricsdata.com</span><span class="foot__num">04</span></div>
</section>

<!-- 05 divider -->
<section class="slide slide--dark col-l row-3">
  <div class="brand brand--tr"><span class="brand__dot"></span>KTLwave</div>
  <h2 class="divider__title">SECTION DIVIDER</h2>
  <div class="foot"><span><span class="foot__ico">&#9742;</span>555-010-4821</span><span class="foot__sep">|</span><span><span class="foot__ico">&#9993;</span>info@ktlwave.com</span><span class="foot__sep">|</span><span><span class="foot__ico">&#9679;</span>https://fanmetricsdata.com</span><span class="foot__num">05</span></div>
</section>

<!-- 06 chart -->
<section class="slide col-r row-3">
  <div class="band">SPORTS FAN SOCIAL MEDIA ENGAGEMENT</div>
  <div class="brand brand--tr"><span class="brand__dot"></span>KTLwave</div>
  <p class="chart__cap">% of fans using social media platform in past 12 months</p>
  <svg class="chart" width="310" height="150" viewBox="0 0 310 150" font-family="Poppins, sans-serif" font-size="4.4" fill="#333">
    <g stroke="var(--grid)" stroke-width=".5">
      <line x1="20" y1="2" x2="302" y2="2"/><line x1="20" y1="24" x2="302" y2="24"/><line x1="20" y1="46" x2="302" y2="46"/>
      <line x1="20" y1="68" x2="302" y2="68"/><line x1="20" y1="90" x2="302" y2="90"/><line x1="20" y1="112" x2="302" y2="112"/>
      <line x1="20" y1="132" x2="302" y2="132"/>
      <line x1="20" y1="2" x2="20" y2="132"/><line x1="67" y1="2" x2="67" y2="132"/><line x1="114" y1="2" x2="114" y2="132"/>
      <line x1="161" y1="2" x2="161" y2="132"/><line x1="208" y1="2" x2="208" y2="132"/><line x1="255" y1="2" x2="255" y2="132"/><line x1="302" y1="2" x2="302" y2="132"/>
    </g>
    <g text-anchor="end">
      <text x="13" y="4">120</text><text x="13" y="26">100</text><text x="13" y="48">80</text><text x="13" y="70">60</text>
      <text x="13" y="92">40</text><text x="13" y="114">20</text><text x="13" y="134">0</text>
    </g>
    <g fill="var(--bar-a)">
      <rect x="35" y="24" width="5" height="108"/><rect x="83" y="35" width="5" height="97"/><rect x="129" y="78" width="5" height="54"/>
      <rect x="177" y="24" width="5" height="108"/><rect x="225" y="24" width="5" height="108"/><rect x="271" y="68" width="5" height="64"/>
    </g>
    <g fill="var(--bar-b)">
      <rect x="44" y="35" width="5" height="97"/><rect x="92" y="46" width="5" height="86"/><rect x="138" y="24" width="5" height="108"/>
      <rect x="186" y="68" width="5" height="64"/><rect x="234" y="35" width="5" height="97"/><rect x="280" y="51" width="5" height="81"/>
    </g>
    <g text-anchor="middle">
      <text x="37.5" y="21">100</text><text x="46.5" y="32">90</text><text x="85.5" y="32">90</text><text x="94.5" y="43">80</text>
      <text x="131.5" y="75">50</text><text x="140.5" y="21">100</text><text x="179.5" y="21">100</text><text x="188.5" y="65">60</text>
      <text x="227.5" y="21">100</text><text x="236.5" y="32">90</text><text x="273.5" y="65">60</text><text x="282.5" y="48">75</text>
    </g>
    <g text-anchor="middle" font-weight="500">
      <text x="43" y="141">CHATTERLY</text><text x="90" y="141">PEEPLO</text><text x="136" y="141">FLASHBOX</text>
      <text x="184" y="141">PICTORA</text><text x="232" y="141">VIDSPAN</text><text x="278" y="141">CLIPZY</text>
    </g>
  </svg>
  <div class="foot"><span>&#9742; 555-010-4821</span><span class="foot__sep">|</span><span>&#9993; info@ktlwave.com</span><span class="foot__sep">|</span><span>&#9679; https://fanmetricsdata.com</span><span class="foot__num">06</span></div>
</section>

<!-- 07 executive summary -->
<section class="slide col-l row-4">
  <div class="band">EXECUTIVE SUMMARY- 3</div>
  <div class="brand brand--tr"><span class="brand__dot"></span>KTLwave</div>
  <div class="card card--blue">
    <span class="card__badge"><svg width="14" height="14"><rect x="2" y="1" width="10" height="12" rx="1" fill="none" stroke="#fff" stroke-width="1.2"/><path d="M5 10V8M7 10V6M9 10V7" stroke="#fff" stroke-width="1.2"/></svg></span>
    <h3 class="card__head">EPILOGUE</h3>
    <p class="card__body">Looking backwards to get a handle on what will happen in the future with respect to sports fandom and related categories is no longer an option. The pandemic of 2020 has erased what we all knew and now means we need to start looking at the present, to get any sort of an idea on the future. The data and insights presented in this report are just the tip on the iceberg when it comes to the level of data granularity. Much of the data is available via the Fan Metrics Data Platform powered by KTLwave.</p>
  </div>
  <div class="card card--orange">
    <span class="card__badge"><svg width="14" height="14"><circle cx="7" cy="6" r="4" fill="none" stroke="#fff" stroke-width="1.2"/><path d="M4.5 9l-1 4 3.5-2 3.5 2-1-4" fill="none" stroke="#fff" stroke-width="1.1"/></svg></span>
    <h3 class="card__head">ACKNOWLEDGEMENTS</h3>
    <p class="card__body">Thank you to everyone that contributed to the 2021 Annual Sports Fan Study and this summary report from KTLwave. A special thanks goes out to Maren Doyle from Calder Field Partners for her help in creating the data tables and data charts used in this report along with our graphics team.</p>
  </div>
  <div class="foot"><span>&#9742; 555-010-4821</span><span class="foot__sep">|</span><span>&#9993; info@ktlwave.com</span><span class="foot__sep">|</span><span>&#9679; https://fanmetricsdata.com</span><span class="foot__num">07</span></div>
</section>

<!-- 08 contact -->
<section class="slide slide--dark col-r row-4">
  <div class="brand brand--tr"><span class="brand__dot"></span>KTLwave</div>
  <h2 class="info__title">FOR MORE<br>INFORMATION</h2>
  <div class="info__rule"></div>
  <p class="info__copy">KTLwave and the Fan Metrics Data Platform provide a comprehensive online platform of nationwide sports business data focused on sports fans and sports participation for analytics, sports marketing, and strategic planning. KTLwave uses syndicated custom and proprietary research for professional and college sports, consumer research, industry reports, and licensed industry articles.</p>
  <p class="info__price">Report Price: <b>$499.00</b></p>
  <div class="info__split"></div>
  <div class="info__row" style="top:72px"><span class="info__ico"><svg width="10" height="10"><path d="M2 1.5l2 0 .8 2-1.2 1c.6 1.2 1.4 2 2.6 2.6l1-1.2 2 .8v2c-4.5 0-7.2-2.7-7.2-7.2z" fill="var(--orange)"/></svg></span>555-010-4821</div>
  <div class="info__row" style="top:99px"><span class="info__ico"><svg width="10" height="10"><rect x="1" y="2.5" width="8" height="5.5" fill="var(--orange)"/><path d="M1 2.5l4 3 4-3" fill="none" stroke="#fff" stroke-width=".8"/></svg></span>info@ktlwave.com</div>
  <div class="info__row" style="top:121px"><span class="info__ico"><svg width="10" height="10"><path d="M5 9.5C2.5 6.5 2 5 2 4a3 3 0 0 1 6 0c0 1-.5 2.5-3 5.5z" fill="var(--orange)"/><circle cx="5" cy="4" r="1.1" fill="#fff"/></svg></span>Contact: Dale Hartman, President of<br>KTLwave</div>
  <div class="info__row" style="top:152px"><span class="info__ico"><svg width="10" height="10"><circle cx="5" cy="5" r="4" fill="var(--orange)"/></svg></span>https://fanmetricsdata.com</div>
</section>

</body>
</html>
```